Harwell Properties Business Cards

I would like a business card that includes myself and my partner.
Includes: Logo, office #, email, website, our names, our numbers and possibly the address. I would also like the logo to be embossed and the card to be horizontal.
There is a photo of our yard signs to give you an idea of the colors of our business.

Target Market(s)

Everyone in real estate market.
We are in a rural area. Our clientele are from all socioeconomic backgrounds.

Industry/Entity Type

Real Estate Agent

Contact Information for Business Card

Company Name: Harwell Properties
Our Names, Titles & Cell #'s : Dana Harwell-Broker (555).613.2947, Marla Harwell-Realtor (555).730.5816
Office #: (555).264.1300
Website: harwellproperties.example
Joint Email: harwell@harwellproperties.example
Office Address: 418C W. Pell Creek St.
Lindenford, ST. 00518

Font styles to use
Serif

Requirements
Must have
• HORIZONTAL, Logo, Myself and my partners names, Our cell #'s, our office #, our website, our email address
Nice to have
• Embossed logo, office address, our titles.

```html
<!DOCTYPE html>
<html lang="en">
<head>
<meta charset="utf-8">
<title>Harwell Properties Business Cards</title>
<link rel="stylesheet" href="https://fonts.googleapis.com/css2?family=Montserrat:wght@400;500;600;700&display=swap">
<style>
  :root {
    --purple: #4b0f6e;
    --purple-emboss: #5a2582;
    --olive: #5e583f;
    --olive-text: #6f6a52;
    --white: #ffffff;
    --stage: #e6e4e8;
    --divider: #c9c6cc;
  }
  * { box-sizing: border-box; margin: 0; padding: 0; }
  html, body {
    width: 1200px;
    height: 900px;
    overflow: hidden;
    background: var(--stage);
    font-family: "Montserrat", Arial, sans-serif;
  }
  .sheet { position: relative; width: 1200px; height: 900px; }
  .card {
    position: absolute;
    left: 250px;
    width: 700px;
    height: 400px;
    border-radius: 26px;
    overflow: hidden;
    box-shadow: 0 10px 28px rgba(0,0,0,0.18);
  }

  /* Back of card */
  .card-back { top: 35px; background: var(--purple); }
  .card-back .emboss-name {
    position: absolute;
    left: 0; right: 0; top: 120px;
    text-align: center;
    font-weight: 600;
    font-size: 58px;
    letter-spacing: 1px;
    color: var(--purple-emboss);
  }
  .card-back .emboss-rule {
    position: absolute;
    left: 200px; right: 200px; top: 208px;
    height: 2px;
    background: var(--purple-emboss);
  }
  .card-back .back-url {
    position: absolute;
    right: 60px; bottom: 44px;
    font-size: 22px;
    font-weight: 500;
    color: var(--white);
    letter-spacing: 0.3px;
  }
  .card-back .back-url b { font-weight: 700; }

  /* Front of card */
  .card-front { top: 465px; background: var(--white); }
  .brand-mark {
    position: absolute;
    left: 40px; top: 110px;
    width: 260px;
    display: flex;
    align-items: center;
    gap: 14px;
  }
  .brand-mark .dot {
    width: 22px; height: 22px;
    flex: none;
    border-radius: 50%;
    background: var(--purple);
  }
  .brand-mark .brand-name {
    font-weight: 700;
    font-size: 30px;
    line-height: 1.1;
    color: var(--purple);
  }
  .divider {
    position: absolute;
    left: 322px; top: 40px;
    width: 2px; height: 200px;
    background: linear-gradient(to bottom, rgba(201,198,204,0), var(--divider) 25%, var(--divider) 75%, rgba(201,198,204,0));
  }
  .contact {
    position: absolute;
    left: 345px; top: 36px; right: 20px;
    color: var(--olive-text);
    font-size: 15px;
    line-height: 1.25;
  }
  .person { margin-bottom: 6px; }
  .person-name { font-weight: 700; font-size: 24px; color: var(--purple); line-height: 1.1; }
  .person-title { font-size: 15px; color: var(--olive-text); }
  .person-phone { font-size: 16px; color: var(--purple); }
  .address { margin-top: 4px; font-size: 15px; color: var(--purple); }
  .office-lines { margin-top: 4px; list-style: none; }
  .office-lines li {
    display: flex;
    align-items: center;
    gap: 8px;
    font-size: 15px;
    color: var(--purple);
  }
  .office-lines svg { width: 12px; height: 12px; flex: none; fill: var(--olive); }
  .office-lines .web { color: var(--olive); font-weight: 500; }
  .office-lines .web b { font-weight: 700; }

  .band-purple {
    position: absolute;
    left: 0; width: 440px; top: 305px;
    height: 12px;
    background: var(--purple);
  }
  .band-olive {
    position: absolute;
    left: 448px; right: 0; top: 305px;
    height: 12px;
    background: var(--olive);
  }
  .band-purple-base {
    position: absolute;
    left: 0; right: 0; bottom: 0;
    height: 34px;
    background: var(--purple);
  }
</style>
</head>
<body>
<main class="sheet">

  <section class="card card-back" aria-label="Card back">
    <p class="emboss-name">Harwell Properties</p>
    <div class="emboss-rule"></div>
    <p class="back-url">www.<b>harwellproperties</b>.example</p>
  </section>

  <section class="card card-front" aria-label="Card front">
    <div class="brand-mark">
      <span class="dot"></span>
      <span class="brand-name">Harwell Properties</span>
    </div>

    <div class="divider"></div>

    <div class="contact">
      <div class="person">
        <p class="person-name">Dana Harwell</p>
        <p class="person-title">Broker</p>
        <p class="person-phone">(555).613.2947</p>
      </div>
      <div class="person">
        <p class="person-name">Marla Harwell</p>
        <p class="person-title">Realtor</p>
        <p class="person-phone">(555).730.5816</p>
      </div>
      <p class="address">418C W. Pell Creek St.<br>Lindenford, ST. 00518</p>
      <ul class="office-lines">
        <li>
          <svg viewBox="0 0 12 12" aria-hidden="true"><path d="M2.5 0.8l2 2.4-1.1 1.3c.7 1.5 1.8 2.6 3.3 3.3l1.3-1.1 2.4 2-1.3 2.4C5 10.8 1.2 7 .1 2.1z"/></svg>
          <span>(555).264.1300</span>
        </li>
        <li>
          <svg viewBox="0 0 12 12" aria-hidden="true"><path d="M0 2h12v8H0zM1 3v.4l5 3.3 5-3.3V3zm0 1.6V9h10V4.6L6 7.9z"/></svg>
          <span>harwell@harwellproperties.example</span>
        </li>
        <li class="web">
          <svg viewBox="0 0 12 12" aria-hidden="true"><path d="M6 0a6 6 0 100 12A6 6 0 006 0zm0 1c.6.7 1.1 1.8 1.3 3H4.7C4.9 2.8 5.4 1.7 6 1zM1.2 5h2.4v2H1.2a5 5 0 010-2zm3.4 0h2.8v2H4.6zm3.8 0h2.4a5 5 0 010 2H8.4zM4.7 8h2.6C7.1 9.2 6.6 10.3 6 11c-.6-.7-1.1-1.8-1.3-3z"/></svg>
          <span>www.<b>harwellproperties</b>.example</span>
        </li>
      </ul>
    </div>

    <div class="band-purple"></div>
    <div class="band-olive"></div>
    <div class="band-purple-base"></div>
  </section>

</main>
</body>
</html>
```